Business Card Design

I am starting my therapy private practice. I will be an in home therapist, so I go into family's homes instead of using an office to do family/marriage therapy. Therefore, I do not have an office address. I am looking for something in the black, red, gray, and blue color scheme that appeals to both families, couples and teenagers.

Industry/Entity Type

Business

Contact Information for Business Card

Lena Brovick, MS, MFT Intern
Marriage and Family Therapy
In Home Therapist
508-241-6039
Lena@LenaBrovick.net

```html
<!DOCTYPE html>
<html lang="en">
<head>
<meta charset="utf-8">
<title>Lena Brovick – Business Card</title>
<link rel="stylesheet" href="https://fonts.googleapis.com/css2?family=Marcellus&display=swap">
<style>
  :root {
    --page: #ffffff;
    --navy: #002d6b;
    --rose: #e3175c;
    --white: #ffffff;
    --icon: #9ccbf0;
    --rule: #c9d6ea;
  }
  * { margin: 0; padding: 0; box-sizing: border-box; }
  html, body {
    width: 1200px;
    height: 695px;
    overflow: hidden;
    background: var(--page);
  }
  .card {
    position: absolute;
    left: 177px;
    top: 101px;
    width: 854px;
    height: 499px;
    background: var(--navy);
    font-family: "Marcellus", "Optima", serif;
    color: var(--white);
  }
  .identity {
    position: absolute;
    left: 40px;
    top: 105px;
    width: 340px;
    text-align: center;
  }
  .identity-mark {
    display: block;
    width: 44px;
    height: 44px;
    margin: 0 auto 120px;
    border: 4px solid var(--rose);
  }
  .identity-name {
    font-size: 38px;
    font-variant: small-caps;
    letter-spacing: 1px;
    line-height: 1;
  }
  .identity-role {
    margin-top: 10px;
    font-size: 16px;
    letter-spacing: 0.1px;
  }
  .ribbon {
    position: absolute;
    left: 414px;
    top: 176px;
    width: 400px;
    height: 46px;
  }
  .ribbon svg { position: absolute; inset: 0; }
  .ribbon-text {
    position: absolute;
    inset: 0;
    display: flex;
    align-items: center;
    justify-content: center;
    font-size: 23px;
    letter-spacing: 1.2px;
    padding-left: 8px;
  }
  .ribbon-heart { font-size: 15px; margin: 0 8px; }
  .contact {
    position: absolute;
    left: 413px;
    top: 237px;
    width: 390px;
    list-style: none;
  }
  .contact-item {
    display: flex;
    align-items: center;
    height: 52px;
    padding-left: 16px;
    border-bottom: 2px dashed var(--rule);
    font-size: 22px;
    letter-spacing: 0.8px;
  }
  .contact-item svg {
    width: 20px;
    height: 20px;
    margin-right: 16px;
    flex: none;
  }
</style>
</head>
<body>
  <main class="card">
    <section class="identity">
      <span class="identity-mark" aria-hidden="true"></span>
      <h1 class="identity-name">Lena Brovick</h1>
      <p class="identity-role">MFT Intern Marriage and Family Therapy</p>
    </section>

    <div class="ribbon">
      <svg viewBox="0 0 400 46" width="400" height="46" aria-hidden="true">
        <polygon points="0,0 400,0 376,23 400,46 0,46 24,23" fill="var(--rose)"/>
      </svg>
      <p class="ribbon-text"><span class="ribbon-heart">♥</span>IN HOME THERAPIST<span class="ribbon-heart">♥</span></p>
    </div>

    <ul class="contact">
      <li class="contact-item">
        <svg viewBox="0 0 20 20" aria-hidden="true">
          <circle cx="10" cy="10" r="8.8" fill="none" stroke="var(--icon)" stroke-width="1.4"/>
          <path d="M7 5.5c-.8.4-1.4 1-1.2 2 .5 2.8 3.4 5.7 6.3 6.4 1 .2 1.7-.4 2.1-1.2l-1.7-1.4-1.2.8c-1.2-.6-2.2-1.6-2.8-2.8l.8-1.2z" fill="var(--icon)"/>
        </svg>
        508-241-6039
      </li>
      <li class="contact-item">
        <svg viewBox="0 0 20 20" aria-hidden="true">
          <path d="M2 8l8-5 8 5v9H2z M2 8l8 5 8-5 M2 17l6-5 M18 17l-6-5" fill="none" stroke="var(--icon)" stroke-width="1.3" stroke-linejoin="round"/>
        </svg>
        lena@lenabrovick.net
      </li>
    </ul>
  </main>
</body>
</html>
```